4 Seitiger DIN A4 Flyer für Angebote (DIN A3 gefaltet)
Zielgruppe
Ich handel und montiere z.B. Hochwertige Fenster, Türen und Parkett.
Zielgruppen sind: Architekten, Baufirmen, Hausbauer sowie Hausbesitzer und Sanierer
Aufgabenstellung
Die Farben aus meinem Logo: Grün, Antrazith, Schwarz.
Der 4 Seitige Flyer soll als Aktionsflyer in der Tageszeitung verteilt werden.
Im Innenteil des Flyers sollten Die Parkettböden und 2 Zimmertüren angeboten werden.
Die Texte :
zu den jeweiligen Bildern gehört der qm Preis und der Satz: "zb. Landhausdiele Eiche, geölt Format 2200x180mm, Nutzschicht 2,5mm"
Ansonsten weis ich nicht was noch textlich verkaufsfördernd wäre
Die Rückseite mit Anschrift, Aktions-Treppen Sanierung oder Neubau( ab 1450.- ), Außenverschalung.

```html
<!DOCTYPE html>
<html lang="de">
<head>
<meta charset="utf-8">
<title>Brandt GmbH – Aktionsflyer</title>
<link rel="stylesheet" href="https://fonts.googleapis.com/css2?family=Jost:wght@500;600;700&family=Cormorant+Garamond:ital,wght@1,500&family=Source+Sans+3:wght@300&display=swap">
<style>
  :root {
    --green: #8dc21f;
    --green-soft: rgba(141, 194, 31, 0.6);
    --anthracite: #2b2b2b;
    --paper: #ffffff;
    --text-grey: #4a4a4a;
    --sky-top: #8fb3d6;
    --sky-low: #d9e4ee;
    --wood-light: #a9703f;
    --wood-dark: #5c3519;
  }
  html, body {
    margin: 0;
    padding: 0;
    width: 1200px;
    height: 849px;
    overflow: hidden;
    background: var(--paper);
  }
  .cover {
    position: relative;
    width: 1200px;
    height: 849px;
    background: var(--paper);
    overflow: hidden;
  }
  .hero-shape {
    position: absolute;
    inset: 0;
  }
  .brand {
    position: absolute;
    top: 52px;
    margin: 0;
    font-family: "Jost", sans-serif;
    font-weight: 600;
    font-size: 36px;
    line-height: 1;
    color: var(--anthracite);
  }
  .brand--left { left: 43px; }
  .brand--right { right: 43px; }
  .headline {
    position: absolute;
    left: 644px;
    top: 340px;
    margin: 0;
    font-family: "Jost", sans-serif;
    font-weight: 600;
    font-size: 56px;
    line-height: 61px;
    letter-spacing: 0.01em;
    color: var(--paper);
  }
  .tagline {
    position: absolute;
    left: 646px;
    top: 532px;
    margin: 0;
    font-family: "Cormorant Garamond", serif;
    font-style: italic;
    font-weight: 500;
    font-size: 27px;
    letter-spacing: 0.3em;
    color: var(--paper);
  }
  .price-badge {
    position: absolute;
    left: 1010px;
    top: 642px;
    width: 148px;
    height: 148px;
    border-radius: 50%;
    background: var(--green);
    color: var(--paper);
    font-family: "Jost", sans-serif;
    text-align: center;
    transform: rotate(-8deg);
  }
  .price-badge__label {
    display: block;
    margin-top: 42px;
    font-size: 15px;
    font-weight: 500;
    letter-spacing: 0.12em;
  }
  .price-badge__amount {
    display: block;
    font-size: 38px;
    font-weight: 600;
    line-height: 1.05;
  }
  .imprint {
    position: absolute;
    left: 43px;
    top: 700px;
    margin: 0;
    font-family: "Source Sans 3", sans-serif;
    font-weight: 300;
    font-size: 13.5px;
    line-height: 18.2px;
    color: var(--text-grey);
    font-style: normal;
  }
</style>
</head>
<body>
<main class="cover">
  <svg class="hero-shape" width="1200" height="849" viewBox="0 0 1200 849">
    <defs>
      <linearGradient id="heroTones" x1="0" y1="0" x2="0" y2="1">
        <stop offset="0" stop-color="var(--sky-top)"/>
        <stop offset="0.2" stop-color="var(--sky-low)"/>
        <stop offset="0.3" stop-color="var(--wood-light)"/>
        <stop offset="0.75" stop-color="var(--wood-dark)"/>
        <stop offset="1" stop-color="#6b6257"/>
      </linearGradient>
      <clipPath id="heroClip">
        <polygon points="416,0 640,0 1200,168 1200,849 560,849 64,280"/>
      </clipPath>
    </defs>
    <polygon role="img" aria-label="Foto: Neubau mit horizontaler Holz-Außenverschalung und großen Glasfronten vor blauem Himmel"
             points="416,0 640,0 1200,168 1200,849 560,849 64,280" fill="url(#heroTones)"/>
    <g clip-path="url(#heroClip)">
      <polygon class="accent-band" points="110,280 165,280 565,849 490,849" fill="var(--green-soft)"/>
      <polygon class="light-band" points="230,170 260,170 455,0 420,0" fill="rgba(190,230,235,0.45)"/>
    </g>
  </svg>

  <p class="brand brand--left">Brandt</p>
  <p class="brand brand--right">Brandt</p>

  <h1 class="headline">HOCHWERTIGE<br>TÜREN, FENSTER<br>UND PARKETT.</h1>
  <p class="tagline">Von Ihrem Spezialisten.</p>

  <div class="price-badge">
    <span class="price-badge__label">NEUBAU ab</span>
    <span class="price-badge__amount">1450€</span>
  </div>

  <address class="imprint">
    Verfasst durch:<br>
    Brandt GmbH<br>
    Lindenweg 48<br>
    81245 München<br>
    T +49 89 274 118 60<br>
    www.brandt-fenster.de
  </address>
</main>
</body>
</html>
```